Google Form Graphic to suit our Brand and industry

Create a graphic / image for us to put at the top of our client enquiry google form.
The image will be a section of an architectural home with our branding over the top. Preferably translucent.
The image must suit the shape of the google forms image, which is an elongated rectangle
#003d5d - brand colour

Target Market(s)

residential home owners, high end architectural homes

Industry/Entity Type

Residential construction

Colors
0054AA
0677BA
7BADD7
CADEEF
E8F1F8

Requirements
Must have
• our branding and a photo of an architectural home in the background

```html
<!DOCTYPE html>
<html lang="en">
<head>
<meta charset="utf-8">
<title>Harbourline Homes – Form Header Banner</title>
<link rel="stylesheet" href="https://fonts.googleapis.com/css2?family=Montserrat:wght@500&display=swap">
<style>
  :root {
    --stage: #d9d9d9;
    --brand-navy: #003d5d;
    --paper: #ffffff;
    --glass-sky: #9fb8c8;
    --glass-mid: #5d7484;
    --glass-dark: #2d3a40;
    --house-sky: #eef3f7;
    --house-wall: #b9c2c9;
    --house-wood: #8a6a4e;
  }
  html, body {
    margin: 0;
    padding: 0;
    width: 1200px;
    height: 675px;
    overflow: hidden;
    background: var(--stage);
  }
  .canvas {
    width: 1200px;
    height: 675px;
    display: flex;
    align-items: center;
    justify-content: center;
  }
  .form-header {
    width: 1080px;
    height: 270px;
    display: block;
  }
  .brand-name {
    font-family: "Montserrat", sans-serif;
    font-weight: 500;
    font-size: 54px;
    letter-spacing: 1px;
    fill: var(--brand-navy);
  }
</style>
</head>
<body>
<main class="canvas">
  <svg class="form-header" viewBox="0 0 1600 400" xmlns="http://www.w3.org/2000/svg">
    <defs>
      <linearGradient id="glassFacade" x1="0" y1="0" x2="0.4" y2="1">
        <stop offset="0" stop-color="var(--glass-sky)"/>
        <stop offset="0.45" stop-color="var(--glass-mid)"/>
        <stop offset="0.85" stop-color="var(--glass-dark)"/>
        <stop offset="1" stop-color="#4f9db5"/>
      </linearGradient>
      <linearGradient id="modernHouse" x1="0" y1="0" x2="1" y2="1">
        <stop offset="0" stop-color="var(--house-sky)"/>
        <stop offset="0.5" stop-color="var(--house-wall)"/>
        <stop offset="1" stop-color="var(--house-wood)"/>
      </linearGradient>
      <linearGradient id="houseFade" x1="0" y1="0" x2="1" y2="0">
        <stop offset="0" stop-color="#fff" stop-opacity="0"/>
        <stop offset="0.35" stop-color="#fff" stop-opacity="1"/>
      </linearGradient>
      <mask id="houseMask">
        <rect x="1000" y="0" width="600" height="400" fill="url(#houseFade)"/>
      </mask>
    </defs>

    <rect class="banner-ground" width="1600" height="400" fill="var(--paper)"/>

    <rect class="photo-glass-building" role="img" aria-label="Photo of a glass-fronted modern home with a pool"
          x="0" y="0" width="520" height="400" fill="url(#glassFacade)"/>

    <rect class="photo-modern-house" role="img" aria-label="Photo of a contemporary house with timber cladding and cantilevered roof"
          x="1000" y="0" width="600" height="400" fill="url(#modernHouse)" mask="url(#houseMask)"/>

    <path class="accent-band" d="M360 0 H560 L480 400 H280 Z" fill="var(--brand-navy)"/>

    <rect class="brand-square" x="560" y="178" width="34" height="34" fill="var(--brand-navy)"/>
    <text class="brand-name" x="618" y="214">Harbourline Homes</text>
  </svg>
</main>
</body>
</html>
```